Ledgrix Business Card

We need a business card design using the attached logo. The company is a financial services company that provides a dashboard (chart based information) for Executives of small businesses to use to better manage their information. The design must be progressive, make good utilization of the logo and project stability and financial security.

Industry/Entity Type

Financial

```html
<!DOCTYPE html>
<html lang="en">
<head>
<meta charset="utf-8">
<title>Ledgrix Business Card</title>
<link rel="stylesheet" href="https://fonts.googleapis.com/css2?family=Questrial&family=Arimo:wght@400;700&display=swap">
<style>
  :root {
    --bg: #ececea;
    --card: #fbfbfb;
    --card-edge: #e2e2e2;
    --red: #9e1b1f;
    --ink: #1c1c1c;
    --faint: #f0f0f0;
  }
  * { box-sizing: border-box; margin: 0; padding: 0; }
  html, body { width: 1200px; height: 784px; overflow: hidden; }
  body {
    background: var(--bg);
    display: flex;
    align-items: center;
    justify-content: center;
    gap: 40px;
    font-family: "Questrial", sans-serif;
    color: var(--ink);
  }
  .card {
    position: relative;
    width: 540px;
    height: 309px;
    background: linear-gradient(160deg, #ffffff 0%, var(--card) 60%, #f3f3f3 100%);
    border: 1px solid var(--card-edge);
    box-shadow: 0 6px 18px rgba(0,0,0,.12);
    overflow: hidden;
  }
  .card-back .mark-faint {
    position: absolute;
    left: 50%; top: 50%;
    width: 170px; height: 170px;
    transform: translate(-50%, -56%);
    border: 14px solid var(--faint);
    border-radius: 16px;
  }
  .holder {
    position: absolute;
    right: 28px; top: 22px;
    text-align: right;
  }
  .holder-name {
    font-family: "Arimo", sans-serif;
    font-weight: 700;
    font-size: 14px;
    color: var(--red);
  }
  .holder-role {
    font-family: "Arimo", sans-serif;
    font-size: 10px;
    color: var(--ink);
    margin-top: 1px;
  }
  .brand {
    position: absolute;
    left: 30px; top: 90px;
    display: flex;
    align-items: center;
    gap: 12px;
  }
  .brand-square {
    width: 44px; height: 44px;
    background: var(--red);
    border-radius: 5px;
  }
  .brand-name {
    font-size: 46px;
    line-height: 1;
    color: var(--ink);
  }
  .rule {
    position: absolute;
    left: 0; right: 0; top: 158px;
    height: 4px;
    background: var(--red);
  }
  .contacts {
    position: absolute;
    left: 30px; top: 186px;
    list-style: none;
    font-size: 17px;
    line-height: 21px;
  }
  .contacts li { display: flex; align-items: flex-start; gap: 8px; }
  .contacts .indent { padding-left: 24px; }
  .contacts .email { margin-top: 8px; }
  .icon { width: 16px; height: 16px; margin-top: 2px; flex: none; fill: var(--red); }
</style>
</head>
<body>
  <section class="card card-back" aria-label="Card back">
    <div class="mark-faint"></div>
  </section>

  <section class="card card-front" aria-label="Card front">
    <div class="holder">
      <div class="holder-name">Dana Whitfield</div>
      <div class="holder-role">Manager</div>
    </div>

    <div class="brand">
      <div class="brand-square"></div>
      <div class="brand-name">Ledgrix</div>
    </div>

    <div class="rule"></div>

    <ul class="contacts">
      <li>
        <svg class="icon" viewBox="0 0 16 16"><path d="M3 1l3 3-1.6 2a9 9 0 0 0 5.6 5.6L12 10l3 3-2 2C7 15 1 9 1 3z"/></svg>
        <span>713-555-0142</span>
      </li>
      <li>
        <svg class="icon" viewBox="0 0 16 16"><rect x="4" y="1" width="8" height="5"/><rect x="1" y="6" width="14" height="6" rx="1"/><rect x="4" y="11" width="8" height="4"/></svg>
        <span>713-555-0187</span>
      </li>
      <li>
        <svg class="icon" viewBox="0 0 16 16"><path d="M8 1l7 7h-2v7H9v-4H7v4H3V8H1z"/></svg>
        <span>4180 Marlow</span>
      </li>
      <li class="indent"><span>Houston, TX 77024</span></li>
      <li class="email">
        <svg class="icon" viewBox="0 0 16 16"><path d="M1 3h14v10H1z M2 4l6 5 6-5" fill="var(--red)" stroke="#fff" stroke-width="1"/></svg>
        <span>d.whitfield@ledgrixconsulting.com</span>
      </li>
    </ul>
  </section>
</body>
</html>
```